create a webpage for optometry practice

I'm looking to create a professional and elegant webpage for my practice. I prefer neutral earthy colors, but I am open to other ideas. I have included an image of my logo to be used in the process. This will be a page that will illustrate information about my practice and the kind of services we offer. I am in process of having the practice remodeled. So I don't have any photos of my practice to include yet.

Target Market(s)

My practice serves young and mature families.

Industry/Entity Type

It Professional

Number of Pages Required

5+ page

Font styles to use
Sans Serif

Colors
33a6d7
86cfc6
85cae6
cadf82
3276b5
faa54b
abd036
f78c1e

Requirements
Must have
• I would need to incorporate information about my practice, services, insurance accepted, make appointment, contact us, and about our family.
Nice to have
• I would like to see something fresh, modern, and unique

```html
<!DOCTYPE html>
<html lang="en">
<head>
<meta charset="utf-8">
<title>Lumen Eye Care</title>
<link rel="stylesheet" href="https://fonts.googleapis.com/css2?family=Roboto:wght@400;500;700&display=swap">
<style>
:root{
  --teal:#1a9ca9;
  --teal-dark:#168894;
  --orange:#dc6a20;
  --orange-dark:#b85314;
  --orange-nav:#e2772a;
  --blue:#3ea3e3;
  --ink:#2a2a2a;
  --muted:#555;
  --line:#e3e3e3;
  --white:#fff;
}
*{box-sizing:border-box;margin:0;padding:0}
html,body{width:1200px;height:2222px;overflow:hidden;background:var(--white)}
body{position:relative;font-family:'Roboto',sans-serif;color:var(--ink)}
.abs{position:absolute}

/* header */
.brand{left:86px;top:28px;display:flex;align-items:center;gap:10px}
.brand-dot{width:22px;height:22px;border-radius:50%;background:var(--orange)}
.brand-name{font-size:28px;font-weight:500;color:var(--teal);letter-spacing:.5px}
.nav{top:38px;font-size:15px;color:var(--orange-nav)}
.nav.active{color:var(--teal);font-weight:500}

/* hero */
.hero{left:0;top:99px;width:1200px;height:434px;
  background:linear-gradient(100deg,#c9a46a 0%,#e8d2a8 28%,#f1ece4 55%,#d9d7d6 72%,#8f8a8a 100%)}
.hero-box{left:316px;top:385px;width:553px;height:148px;background:rgba(26,156,169,.85)}
.hero-title{left:462px;top:400px;color:var(--white);font-weight:700;font-size:42px;line-height:50px}
.hero-sub{left:462px;top:450px;color:var(--white);font-weight:500;font-size:30px}
.dots{left:466px;top:512px;display:flex;gap:8px}
.dots span{width:9px;height:9px;background:var(--white)}
.dots span:first-child{background:var(--orange)}

/* services */
.service{width:247px;text-align:center}
.service-icon{width:114px;height:114px;border-radius:50%;background:var(--blue);margin:0 auto;display:flex;align-items:center;justify-content:center}
.service h3{font-size:20px;font-weight:700;margin:20px 0 8px}
.service p{font-size:13.5px;line-height:19px;color:var(--ink)}
.divider{left:86px;top:876px;width:1028px;height:1px;background:var(--line)}

/* news */
.news-title{left:86px;top:940px;font-size:25px;font-weight:500;color:var(--teal)}
.news-photo{left:86px;width:126px;height:94px}
.news-text{left:230px;width:330px}
.news-text h4{font-size:15px;font-weight:500;color:var(--teal)}
.news-text time{display:block;font-size:10px;color:var(--teal);margin:5px 0 6px}
.news-text p{font-size:11px;line-height:18px;color:var(--muted)}

/* appointment */
.form{left:637px;top:928px;width:477px;height:326px;border:1px solid var(--line);box-shadow:0 1px 4px rgba(0,0,0,.12)}
.form-head{height:50px;background:var(--orange);color:var(--white);font-size:23px;font-weight:500;padding:10px 14px}
.field{width:210px;height:28px;display:flex;align-items:center;border:1px solid #d8d8d8}
.field .ico{width:28px;height:28px;background:var(--orange);display:flex;align-items:center;justify-content:center;flex:none}
.field span.label{font-size:12px;color:#888;padding-left:10px;flex:1}
.field .caret{width:0;height:0;border-left:5px solid transparent;border-right:5px solid transparent;border-top:6px solid #888;margin-right:8px}
.submit{left:807px;top:1210px;width:144px;height:26px;background:var(--orange);color:var(--white);font-size:14px;display:flex;align-items:center;justify-content:center}

/* feature block */
.feature{left:86px;top:1309px;width:1028px;height:400px;background:var(--teal)}
.feature-photo{left:118px;top:1358px;width:430px;height:291px;border:5px solid var(--white);
  background:linear-gradient(120deg,#f2f2f2 0%,#d7dde2 40%,#9aa3ab 75%,#4c5259 100%)}
.feature-title{left:595px;top:1352px;font-size:21px;font-weight:700;color:var(--white)}
.feature-text{left:595px;top:1390px;width:500px;font-size:12.8px;line-height:26px;color:var(--white)}

/* slider */
.slider{left:86px;top:1770px;width:1028px;height:151px;
  background:linear-gradient(90deg,#5a5552 0%,#9c948d 30%,#b7ada3 55%,#8c837c 78%,#4e4a47 100%)}
.slider-title{left:86px;top:1805px;width:1028px;text-align:center;font-size:25px;font-weight:700;color:var(--white)}
.slider-text{left:310px;top:1844px;width:580px;text-align:center;font-size:13px;line-height:24px;color:var(--white)}
.arrow{top:1827px;width:34px;height:34px;border-radius:50%;border:2px solid var(--white);background:rgba(0,0,0,.25);display:flex;align-items:center;justify-content:center}

/* footer */
.footer{left:0;top:1975px;width:1200px;height:247px;background:var(--orange)}
.footer-title{left:0;top:1998px;width:1200px;text-align:center;font-size:25px;font-weight:500;color:var(--white)}
.footer-text{left:360px;top:2038px;width:480px;text-align:center;font-size:16px;line-height:24px;color:var(--white)}
.social{top:2118px;width:40px;height:40px;border-radius:50%;background:var(--white)}
.social i{display:block;width:14px;height:14px;border-radius:50%;background:var(--orange);margin:13px}
.legal{left:0;top:2185px;width:1200px;height:37px;background:var(--orange-dark);color:var(--white);font-size:11px;font-weight:500;text-align:center;line-height:37px}
</style>
</head>
<body>

<header>
  <div class="abs brand"><span class="brand-dot"></span><span class="brand-name">Lumen Eye Care</span></div>
  <nav>
    <a class="abs nav active" style="left:580px">About my practice</a>
    <a class="abs nav" style="left:706px">Services</a>
    <a class="abs nav" style="left:785px">Insurance accepted</a>
    <a class="abs nav" style="left:928px">Make appointment</a>
    <a class="abs nav" style="left:1054px">Contact us</a>
  </nav>
</header>

<section>
  <div class="abs hero" role="img" aria-label="Close-up of a woman wearing dark-framed glasses"></div>
  <div class="abs hero-box"></div>
  <div class="abs hero-title">SOLVING</div>
  <div class="abs hero-sub">VISUAL PROBLEMS</div>
  <div class="abs dots"><span></span><span></span><span></span><span></span></div>
</section>

<section>
  <div class="abs service" style="left:72px;top:585px">
    <div class="service-icon"><svg width="56" height="56" viewBox="0 0 56 56" fill="none" stroke="#fff" stroke-width="4" stroke-linecap="round"><path d="M20 8l12 20M16 46h26M28 46c10 0 14-8 12-16M22 30l10-6"/></svg></div>
    <h3>Lorem Ipsum</h3>
    <p>Contrary to popular belief, Lorem Ipsum is not simply random text. It has roots in a piece of classical Latin literature from 45 BC, making it over 2000 years old.</p>
  </div>
  <div class="abs service" style="left:341px;top:585px">
    <div class="service-icon"><svg width="60" height="40" viewBox="0 0 60 40" fill="none" stroke="#fff" stroke-width="4" stroke-linejoin="round" stroke-linecap="round"><path d="M2 22h14l5-12 7 24 6-18 4 6h20"/></svg></div>
    <h3>Lorem Ipsum</h3>
    <p>Contrary to popular belief, Lorem Ipsum is not simply random text. It has roots in a piece of classical Latin literature from 45 BC, making it over 2000 years old.</p>
  </div>
  <div class="abs service" style="left:613px;top:585px">
    <div class="service-icon"><svg width="56" height="56" viewBox="0 0 56 56" fill="none" stroke="#fff" stroke-width="4" stroke-linecap="round"><path d="M24 6C16 18 10 26 10 34a14 14 0 0 0 20 12"/><circle cx="34" cy="34" r="9"/><path d="M41 41l8 8"/></svg></div>
    <h3>Lorem Ipsum</h3>
    <p>Contrary to popular belief, Lorem Ipsum is not simply random text. It has roots in a piece of classical Latin literature from 45 BC, making it over 2000 years old.</p>
  </div>
  <div class="abs service" style="left:884px;top:585px">
    <div class="service-icon"><svg width="56" height="56" viewBox="0 0 56 56" fill="none" stroke="#fff" stroke-width="4" stroke-linecap="round"><path d="M14 10l8 8-5 6c3 6 8 11 14 14l6-5 8 8-6 6C22 46 10 34 8 16z"/><text x="28" y="26" fill="#fff" stroke="none" font-size="14" font-family="Roboto,sans-serif" font-weight="700">24</text></svg></div>
    <h3>Lorem Ipsum</h3>
    <p>Contrary to popular belief, Lorem Ipsum is not simply random text. It has roots in a piece of classical Latin literature from 45 BC, making it over 2000 years old.</p>
  </div>
  <div class="abs divider"></div>
</section>

<section>
  <h2 class="abs news-title">Latest News</h2>
  <div class="abs news-photo" style="top:993px;background:linear-gradient(90deg,#d7c6b8,#8a6b58)" role="img" aria-label="Woman in glasses talking on the phone"></div>
  <div class="abs news-text" style="top:990px">
    <h4>Lorem Ipsum</h4><time>04.08.2015</time>
    <p>Contrary to popular belief, Lorem Ipsum is not simply random text. It has roots in a piece of classical Latin not simply random text. It has roots in a piece of classical Latin classical Latin</p>
  </div>
  <div class="abs news-photo" style="top:1140px;background:linear-gradient(90deg,#e9e4df,#b9a79a)" role="img" aria-label="Patient receiving an eye examination"></div>
  <div class="abs news-text" style="top:1137px">
    <h4>Lorem Ipsum</h4><time>04.08.2015</time>
    <p>Contrary to popular belief, Lorem Ipsum is not simply random text. It has roots in a piece of classical Latin not simply random text. It has roots in a piece of classical Latin</p>
  </div>
</section>

<section class="abs form">
  <div class="form-head">Appointment Form</div>
</section>
<div class="abs field" style="left:648px;top:1010px"><span class="ico"><svg width="14" height="14" viewBox="0 0 14 14" fill="#fff"><circle cx="7" cy="4" r="3"/><path d="M1 14c0-4 3-6 6-6s6 2 6 6z"/></svg></span><span class="label">Name</span></div>
<div class="abs field" style="left:880px;top:1010px"><span class="ico"><svg width="14" height="14" viewBox="0 0 14 14" fill="#fff"><path d="M2 1l3 3-1 2c1 2 2 3 4 4l2-1 3 3-2 2C5 13 1 9 0 3z"/></svg></span><span class="label">Phone</span></div>
<div class="abs field" style="left:648px;top:1060px"><span class="ico"><svg width="14" height="12" viewBox="0 0 14 12" fill="none" stroke="#fff" stroke-width="1.6"><rect x="1" y="1" width="12" height="10"/><path d="M1 1l6 5 6-5"/></svg></span><span class="label">Email</span></div>
<div class="abs field" style="left:880px;top:1060px"><span class="ico"><svg width="14" height="14" viewBox="0 0 14 14" fill="none" stroke="#fff" stroke-width="1.6"><rect x="1" y="2" width="12" height="11"/><path d="M1 6h12M4 0v3M10 0v3"/></svg></span><span class="label">Today Date</span></div>
<div class="abs field" style="left:648px;top:1110px"><span class="ico"><svg width="14" height="14" viewBox="0 0 14 14" fill="none" stroke="#fff" stroke-width="1.6"><rect x="1" y="2" width="12" height="11"/><path d="M1 6h12M4 0v3M10 0v3"/></svg></span><span class="label">Appointment Date</span></div>
<div class="abs field" style="left:880px;top:1110px"><span class="ico"><svg width="14" height="14" viewBox="0 0 14 14" fill="none" stroke="#fff" stroke-width="1.6"><rect x="1" y="2" width="12" height="11"/><path d="M1 6h12M4 0v3M10 0v3"/></svg></span><span class="label">Date of Birth(mm/dd/yyyy)</span><span class="caret"></span></div>
<div class="abs field" style="left:648px;top:1160px"><span class="ico"><svg width="14" height="14" viewBox="0 0 14 14" fill="none" stroke="#fff" stroke-width="1.6"><circle cx="7" cy="7" r="6"/><path d="M7 3v4l3 2"/></svg></span><span class="label">Timing</span><span class="caret"></span></div>
<div class="abs field" style="left:880px;top:1160px"><span class="ico"><svg width="14" height="14" viewBox="0 0 14 14" fill="#fff"><path d="M5 1h4v4h4v4H9v4H5V9H1V5h4z"/></svg></span><span class="label">Medical Insurance</span><span class="caret"></span></div>
<div class="abs submit">Submit</div>

<section>
  <div class="abs feature"></div>
  <div class="abs feature-photo" role="img" aria-label="Optometrist examining a patient with an eye examination instrument"></div>
  <h2 class="abs feature-title">Contrary to popular</h2>
  <p class="abs feature-text">There are many variations of passages of Lorem Ipsum available, but the majority have suffered alteration in some form, by injected humour, or randomised words which don't look even slightly believable. If you are going to use a passage of Lorem Ipsum, you need to be sure there isn't anything embarrassing hidden in the middle of text. All the Lorem Ipsum generators on the Internet tend to repeat predefined chunks as necessary, making this the first true generator on the Internet. It uses a dictionary of over 200 Latin words, combined with a handful of model sentence structures, to generate Lorem Ipsum which looks reasonable. The generated Lorem Ipsum is therefore always free from repetition, injected humour, or non-characteristic words etc.</p>
</section>

<section>
  <div class="abs slider" role="img" aria-label="Blurred photo of an eye care clinic interior"></div>
  <h2 class="abs slider-title">Contrary to popular belief, Lorem Ipsum</h2>
  <p class="abs slider-text">Contrary to popular belief, Lorem Ipsum is not simply random text. It has roots in a piece of classical Latin literature from 45 BC, making it ove</p>
  <div class="abs arrow" style="left:111px"><svg width="12" height="14" viewBox="0 0 12 14" fill="none" stroke="#fff" stroke-width="2.5"><path d="M9 1L3 7l6 6"/></svg></div>
  <div class="abs arrow" style="left:1055px"><svg width="12" height="14" viewBox="0 0 12 14" fill="none" stroke="#fff" stroke-width="2.5"><path d="M3 1l6 6-6 6"/></svg></div>
</section>

<footer>
  <div class="abs footer"></div>
  <h2 class="abs footer-title">About us</h2>
  <p class="abs footer-text">Lorem ipsum dolor sit amet, consec tetuer adipi scing elit. Praesent vestibulum molestie lacus. Aenean nonummy hendrerit mauris. Phasellus porta. Fusce suscipit varius mi.</p>
  <div class="abs social" style="left:496px"><i></i></div>
  <div class="abs social" style="left:553px"><i></i></div>
  <div class="abs social" style="left:610px"><i></i></div>
  <div class="abs social" style="left:663px"><i></i></div>
  <div class="abs legal">© 2015 Privacy Policy lumeneyecare.com</div>
</footer>

</body>
</html>
```